43 Year Old Construction firm needs Updated Business Card & Stationery Design

We are an established and well known (in our market) commercial construction firm. We need a cleaner and more modern look for our corporate identity material. We would like to continue to use our current colors and logo.
We are thinking about incorporating a slogan on our business card (either front or back): "Striving to be the most trusted builder in our market." The text could change at some point. Our website is www.kradworth.example . Sample card is attached. Some will have more phone numbers, etc...
Updates

Target Market(s)

Commercial and institutional clients.

Industry/Entity Type

Construction Company

Contact Information for Business Card

See attached for existing card. But don't be constrained.

Requirements
Must have
• Logo, name, title, address, website, email, phone numbers (as few as one, as many as three)
• Slogan on front or back "Striving to be the most trusted builder in our market"
• Use existing logo and colors

```html
<!DOCTYPE html>
<html lang="en">
<head>
<meta charset="utf-8">
<title>Kradworth Builders – Business Card</title>
<link rel="stylesheet" href="https://fonts.googleapis.com/css2?family=Arimo:wght@400;700&display=swap">
<style>
  :root {
    --navy: #0d3f7f;
    --navy-deep: #0a2f60;
    --navy-light: #1f5a9e;
    --green: #2fa35a;
    --white: #ffffff;
    --ink: #3b3f45;
    --grey-text: #c9d3e0;
    --backdrop: #e9e6e1;
  }
  * { box-sizing: border-box; margin: 0; padding: 0; }
  html, body { width: 1200px; height: 950px; overflow: hidden; }
  body {
    background: var(--backdrop);
    font-family: "Arimo", Arial, sans-serif;
    position: relative;
  }
  .card {
    position: absolute;
    left: 250px;
    width: 700px;
    height: 400px;
    box-shadow: 0 10px 28px rgba(0,0,0,0.22);
    overflow: hidden;
  }
  /* Back side */
  .card-back {
    top: 50px;
    background: linear-gradient(120deg, var(--navy-deep) 0%, var(--navy) 55%, var(--navy-light) 100%);
    display: flex;
    flex-direction: column;
    align-items: center;
    justify-content: center;
    gap: 22px;
  }
  .card-back .brand-name { color: var(--white); font-size: 50px; }
  .card-back .brand-mark { background: var(--green); }
  .slogan {
    color: var(--grey-text);
    font-size: 19px;
    letter-spacing: 0.3px;
  }
  /* Shared brand lockup */
  .brand {
    display: flex;
    align-items: center;
    gap: 14px;
  }
  .brand-mark {
    width: 26px;
    height: 26px;
    background: var(--navy);
  }
  .brand-name {
    font-weight: 700;
    letter-spacing: 1px;
    text-transform: uppercase;
  }
  /* Front side */
  .card-front {
    top: 500px;
    background: linear-gradient(180deg, #ffffff 0%, #f4f5f7 100%);
  }
  .card-front .brand {
    position: absolute;
    top: 58px;
    left: 0; right: 0;
    justify-content: center;
  }
  .card-front .brand-name { color: var(--navy); font-size: 44px; }
  .name-band {
    position: absolute;
    top: 170px;
    left: 0; right: 0;
    height: 92px;
    background: linear-gradient(90deg, var(--navy-deep), var(--navy) 60%, var(--navy-light));
    border-top: 3px solid var(--green);
    border-bottom: 3px solid var(--green);
    display: flex;
    flex-direction: column;
    align-items: center;
    justify-content: center;
    gap: 6px;
    color: var(--white);
  }
  .person-name { font-size: 24px; font-weight: 700; }
  .person-title { font-size: 18px; }
  .address {
    position: absolute;
    top: 294px;
    left: 0; right: 0;
    text-align: center;
    color: var(--ink);
    font-size: 19px;
    letter-spacing: 0.5px;
  }
  .contacts {
    position: absolute;
    top: 340px;
    left: 0; right: 0;
    display: flex;
    justify-content: center;
    gap: 34px;
    color: var(--ink);
    font-size: 18px;
  }
  .contact-item { display: flex; align-items: center; gap: 8px; }
  .contact-item svg { width: 18px; height: 18px; fill: var(--navy); }
</style>
</head>
<body>

  <section class="card card-back" aria-label="Card back">
    <div class="brand">
      <span class="brand-mark"></span>
      <span class="brand-name">Kradworth Builders</span>
    </div>
    <p class="slogan">Striving to be the most trusted builder in our market.</p>
  </section>

  <section class="card card-front" aria-label="Card front">
    <div class="brand">
      <span class="brand-mark"></span>
      <span class="brand-name">Kradworth Builders</span>
    </div>

    <div class="name-band">
      <p class="person-name">Martin Ellery</p>
      <p class="person-title">President</p>
    </div>

    <p class="address">2840 harbor ridge road, fairmont, MO 63990</p>

    <div class="contacts">
      <span class="contact-item">
        <svg viewBox="0 0 24 24" aria-hidden="true"><path d="M6.6 10.8a15.1 15.1 0 0 0 6.6 6.6l2.2-2.2c.3-.3.7-.4 1-.2 1.1.4 2.3.6 3.6.6.6 0 1 .4 1 1V20c0 .6-.4 1-1 1C10.6 21 3 13.4 3 4c0-.6.4-1 1-1h3.5c.6 0 1 .4 1 1 0 1.3.2 2.5.6 3.6.1.3 0 .7-.2 1z"/></svg>
        555.014.2276
      </span>
      <span class="contact-item">
        <svg viewBox="0 0 24 24" aria-hidden="true"><path d="M2 5h20v14H2zM4 7v.5l8 5 8-5V7zm0 2.8V17h16V9.8l-8 5z"/></svg>
        name@kradworth.example
      </span>
      <span class="contact-item">
        <svg viewBox="0 0 24 24" aria-hidden="true"><path d="M12 2a10 10 0 1 0 0 20 10 10 0 0 0 0-20zm6.9 9h-3a15 15 0 0 0-1.3-6 8 8 0 0 1 4.3 6zM12 4c.9 1.2 1.8 3.7 1.9 7h-3.8c.1-3.3 1-5.8 1.9-7zM9.4 5a15 15 0 0 0-1.3 6h-3a8 8 0 0 1 4.3-6zm-4.3 8h3a15 15 0 0 0 1.3 6 8 8 0 0 1-4.3-6zM12 20c-.9-1.2-1.8-3.7-1.9-7h3.8c-.1 3.3-1 5.8-1.9 7zm2.6-1a15 15 0 0 0 1.3-6h3a8 8 0 0 1-4.3 6z"/></svg>
        www.kradworth.example
      </span>
    </div>
  </section>

</body>
</html>
```